International wholesale business needs a business card

We need a business card.

Company Details:
Company Name and logo
Address, Phone number, Website
Employee Details:
Name, Designation, Mobile Number & Email address

Logo file is attached.

```html
<!DOCTYPE html>
<html lang="en">
<head>
<meta charset="utf-8">
<title>Veloria Trading — Business Card</title>
<link href="https://fonts.googleapis.com/css2?family=Roboto:wght@400;500;700&display=swap" rel="stylesheet">
<style>
  :root {
    --backdrop: #2b2b2b;
    --card-light: #f2f2f2;
    --card-shade: #e2e2e2;
    --brand-red: #b3202a;
    --brand-grey: #868a8e;
    --ink: #222222;
  }
  html, body {
    margin: 0;
    padding: 0;
    width: 1200px;
    height: 1138px;
    overflow: hidden;
    background: var(--backdrop);
    font-family: "Roboto", Arial, sans-serif;
  }
  .canvas {
    position: relative;
    width: 1200px;
    height: 1138px;
  }
  .card {
    position: absolute;
    width: 620px;
    height: 375px;
    border-radius: 16px;
    overflow: hidden;
    background: linear-gradient(180deg, var(--card-light) 0%, #ebebeb 55%, var(--card-shade) 100%);
  }
  .card-front { left: 274px; top: 186px; }
  .card-back  { left: 276px; top: 608px; }

  .brand {
    position: absolute;
    color: var(--brand-red);
    font-weight: 700;
  }
  .brand-name { display: flex; flex-direction: column; line-height: 1; }
  .brand-name .main { letter-spacing: 1px; }
  .brand-name .sub { align-self: flex-end; }

  .card-front .brand { left: 0; right: 0; top: 116px; display: flex; justify-content: center; }
  .card-front .brand-name .main { font-size: 76px; }
  .card-front .brand-name .sub { font-size: 20px; letter-spacing: 12px; margin-top: 8px; margin-right: -12px; }

  .edge-stripe {
    position: absolute;
    left: 0; right: 0; bottom: 0;
    height: 11px;
    display: flex;
  }
  .edge-stripe .red { flex: 1; background: var(--brand-red); }
  .edge-stripe .grey { flex: 1; background: var(--brand-grey); }

  .card-back .brand { right: 34px; top: 38px; }
  .card-back .brand-name .main { font-size: 56px; }
  .card-back .brand-name .sub { font-size: 15px; letter-spacing: 10px; margin-top: 6px; margin-right: -10px; }

  .person { position: absolute; left: 38px; top: 214px; }
  .person-name { margin: 0; font-size: 25px; font-weight: 500; color: var(--brand-red); }
  .person-role { margin: 4px 0 0; font-size: 16.5px; color: var(--ink); }

  .address {
    position: absolute; left: 38px; top: 298px;
    font-style: normal; font-size: 16.5px; line-height: 23px; color: var(--ink);
  }
  .contacts {
    position: absolute; right: 32px; top: 276px;
    list-style: none; margin: 0; padding: 0;
    font-size: 16.5px; color: var(--ink);
  }
  .contacts li {
    display: flex; justify-content: flex-end; align-items: center;
    gap: 14px; height: 23.5px;
  }
  .contacts svg { width: 14px; height: 14px; fill: var(--brand-red); flex: none; }
</style>
</head>
<body>
<main class="canvas">
  <section class="card card-front" aria-label="Card front">
    <div class="brand">
      <span class="brand-name"><span class="main">VELORIA</span><span class="sub">TRADING</span></span>
    </div>
    <div class="edge-stripe"><span class="red"></span><span class="grey"></span></div>
  </section>

  <section class="card card-back" aria-label="Card back">
    <div class="brand">
      <span class="brand-name"><span class="main">VELORIA</span><span class="sub">TRADING</span></span>
    </div>

    <div class="person">
      <h1 class="person-name">John Doe Smith</h1>
      <p class="person-role">Managing Director</p>
    </div>

    <address class="address">234 Anywhere St., Any City,<br>Any Town, US 123456</address>

    <ul class="contacts">
      <li>000-111-1111
        <svg viewBox="0 0 16 16" aria-hidden="true"><path d="M1 5c0-2 3-3 7-3s7 1 7 3v1.5h-3.5V5h-7v1.5H1z"/><path d="M3 8l2-2h6l2 2v6H3z"/></svg>
      </li>
      <li>john@veloriatrading.com
        <svg viewBox="0 0 16 16" aria-hidden="true"><path d="M1 3h14v10H1z M2.5 4.5l5.5 4.5 5.5-4.5" fill="none" stroke="#b3202a" stroke-width="1.8"/><path d="M1 3h14L8 9z"/></svg>
      </li>
      <li>www.veloriatrading.com
        <svg viewBox="0 0 16 16" aria-hidden="true"><circle cx="8" cy="8" r="6.5" fill="none" stroke="#b3202a" stroke-width="1.6"/><path d="M1.5 8h13M8 1.5v13" stroke="#b3202a" stroke-width="1.2"/><ellipse cx="8" cy="8" rx="3" ry="6.5" fill="none" stroke="#b3202a" stroke-width="1.2"/></svg>
      </li>
    </ul>
  </section>
</main>
</body>
</html>
```